Corvelle Beauty Lounge needs a product poster

This poster is advertising our products and services. There are several damask patterns throughout the store. Our store's colors are blue, yellow, white, and gold.However the use of vibrant colors would be great! Our theme is old Hollywood. We have to use this design for our price list, product advertisement, and store promotions poster. Poster 2 and 3 can have the same layout. Poster 1 is different because I want the menu enclosed in a frame with the model resting against it or on top of it. All three posters will be hung on the same wall. I have attached my logo and additional photos for your review. I have also attached a images few posters. To give a better idea. I like how the fonts are not all the same. I like how they used the space. I like the use of color. Also I want the logo small with a white oval background. I don't want our logo to be a focal point.
Poster 1: The menu. This poster should include the blonde sailor either above the menu or beside the menu, 2 images have been included to choose from. I want the area with the prices in some type of decorative frame, with the model on top or on the side. (The model is displaying the prices) Also the model's background is white but I want her background to have color. Green would be great! I also like the idea of having "Now Showing" as part of the frame.
The text should read
" Services
Full Body Application..........................................$35.00
Half Body Application.........................................$20.00
Competition Application......................................$50,00
Face Only...........................................................$10.00
Packages:
4 Tans.... ............................................................$120.00 (Never Expires)
8 Tans ................................................................$200.00 (Never Expires)
Monthly Unlimited...............................................$95.00
Specials:
High School Students .......................................$25.00 EVERYDAY!!
All Day Every Tuesday.......................................$25.00
New Clients........................................................$25.00 (First Visit Only)
(If you want to be creative this section can be separate from the menu or part of the menu. Your choice)
Don't have time to come to us? We also have MOBILE Services! OUR ARTISTS CAN COME TO YOU!
In-Home Party Rates (5 people or more)...........$35.00 per person (Travel Fee Waived)
Poster 2: Kelvane Solution...The image of the pinup with the clock if for this poster.
The text should read:
" PRESSED FOR TIME? Try our KELVANE sunless solution. Rinse in as little as 2 hours" (Pressed for time, Kelvane, and 2 Hours is what we want to stand out)
Poster 3: Packages..The image for this poster is of the girl with the binoculars.
The text should read:
"We offer packages and memberships with UNBELIEVABLE SAVINGS. Tans as low as $20!!" (Unbelievable savings and $20 is what we want to stand out)
I made changes to my briefing. Please let me know if I need to make any other changes or additions
We increased our budget for our design, in order to get more participants
I updated our brief. I have included examples and more detailed instructions. I hope this helps
People who value beauty and glamour. We have an upscale clientele.
Advertising

```html
<!DOCTYPE html>
<html lang="en">
<head>
<meta charset="utf-8">
<title>Kelvane Sunless Solution – Corvelle Beauty Lounge</title>
<link rel="stylesheet" href="https://fonts.googleapis.com/css2?family=Pinyon+Script&family=Prata&family=Libre+Caslon+Text&display=swap">
<style>
  :root{
    --sky:#bcd6d4;
    --sky-deep:#9fc2c3;
    --sky-light:#d6e6e2;
    --ink:#141414;
    --cream:#efe9dc;
    --powder:#9ccbdc;
    --white:#ffffff;
    --coral:#c8322a;
    --skin:#e6c1a6;
  }
  *{margin:0;padding:0;box-sizing:border-box}
  html,body{width:960px;height:1200px;overflow:hidden}
  body{background:var(--sky)}
  .poster{
    position:relative;width:960px;height:1200px;overflow:hidden;
    background:
      radial-gradient(ellipse at 40% 35%, var(--sky-light) 0%, transparent 60%),
      radial-gradient(ellipse at 80% 90%, var(--sky-deep) 0%, transparent 55%),
      linear-gradient(180deg, var(--sky) 0%, var(--sky-deep) 100%);
  }
  .hero-photo{
    position:absolute;left:100px;top:20px;width:840px;height:640px;
    border-radius:46% 40% 12% 30% / 40% 38% 10% 30%;
    background:
      radial-gradient(ellipse at 45% 70%, var(--coral) 0%, rgba(200,50,42,.55) 22%, transparent 40%),
      radial-gradient(ellipse at 30% 35%, var(--skin) 0%, rgba(230,193,166,.6) 30%, transparent 60%),
      radial-gradient(ellipse at 85% 55%, rgba(20,20,20,.55) 0%, transparent 45%);
    opacity:.9;
  }
  .headline{position:absolute;left:510px;top:138px;width:320px;text-align:center;color:var(--ink)}
  .headline-script{font-family:"Pinyon Script",cursive;font-size:64px;line-height:1}
  .headline-caps{font-family:"Prata",serif;font-size:66px;letter-spacing:4px;line-height:1.1;margin-top:4px}

  .try-band{
    position:absolute;left:42px;top:696px;width:440px;height:50px;background:var(--cream);
    font-family:"Prata",serif;font-size:44px;letter-spacing:8px;color:var(--ink);
    padding-left:30px;line-height:52px;
  }
  .product-tag{
    position:absolute;left:452px;top:606px;height:134px;padding:8px 14px 0 14px;background:var(--cream);
  }
  .product-name{
    border:3px solid var(--ink);padding:0 14px;
    font-family:"Prata",serif;font-size:62px;letter-spacing:4px;line-height:82px;color:var(--ink);
  }
  .black-band{position:absolute;left:66px;top:738px;width:828px;height:198px;background:var(--ink)}
  .sunless{
    position:absolute;left:66px;top:762px;width:828px;text-align:center;
    font-family:"Prata",serif;font-size:88px;letter-spacing:26px;color:var(--powder);line-height:1;padding-left:26px;
  }
  .solution{
    position:absolute;left:66px;top:818px;width:828px;text-align:center;
    font-family:"Pinyon Script",cursive;font-size:150px;color:var(--white);line-height:1;
  }
  .rinse-band{
    position:absolute;left:96px;top:934px;width:768px;height:64px;background:var(--cream);
    font-family:"Libre Caslon Text",serif;font-size:36px;letter-spacing:3px;color:var(--ink);
    text-align:center;line-height:66px;
  }
  .brand-mark{
    position:absolute;left:782px;top:1122px;width:144px;height:66px;border-radius:50%;background:var(--white);
    display:flex;align-items:center;justify-content:center;text-align:center;
    font-family:"Prata",serif;font-size:13px;line-height:1.15;color:var(--ink);padding:0 14px;
  }
</style>
</head>
<body>
<main class="poster">
  <div class="hero-photo" role="img" aria-label="Pin-up model in a red corset, polka-dot headscarf and black gloves, looking surprised at an alarm clock, with a black swirl ornament behind her"></div>

  <h1 class="headline">
    <span class="headline-script">Pressed for</span><br>
    <span class="headline-caps">TIME?</span>
  </h1>

  <div class="try-band">TRY OUR</div>
  <div class="product-tag"><div class="product-name">KELVANE</div></div>

  <div class="black-band"></div>
  <div class="sunless">SUNLESS</div>
  <div class="solution">Solution</div>

  <div class="rinse-band">Rinse in as little as 2 hours</div>

  <div class="brand-mark">Corvelle Beauty Lounge</div>
</main>
</body>
</html>
```